Poster for a Theatre production!

Create a poster (11 by 17) promoting an upcoming theatre production. The play is called THE HOLLOW CLOCKWORK by Victor L. Marsh . The play is a fusion of the absurd and realism and has a quantum physics/ mechanics slant fyi. I would like primarily a dark/black background with white print. there should be quantum physics imagery , (squiggly lines/ atoms etc. celestial even...) in the background as well . The
THE HOLLOW CLOCKWORK letters Should Start out white as though ' painted ' (this is important.)and gradually fade to grey or white and black (Still visable though) . To be included also - 'Theatre Velunor presents' (top of poster and about 1/3 the size) then THE HOLLOW CLOCKWORK ' by Victor L Marsh' and Half the size of the Title. Also included in print ' Directed by Martin Kesslow' and the words 'with' Caroline Westby, Tom Ashfeld and and Margaret Okonroy Also in small print 'Video design by Lorna Pettibridge'. The poster also Needs the Dates ' Dec 7-16th ,The Lantern Works , 418 Marlowe Street 555 318-4096 '

Target Market(s)

Theatre going audience

Font styles to use
Other font styles liked:
• white painted effect on THE HOLLOW CLOCKWORK

Colors
1b1b1b
fbfbfb
cbcbcb
dddddd
d5d5d5
5c5c5c
333333

Requirements
Must have
• Theatre Velunor presents THE HOLLOW CLOCKWORK by Victor L Marsh . Directed by Martin Kesslow ( THIS THE CAST FYI)'with' Caroline Westby, Tom Ashfeld, Margarett Okonroyy . Video design by Lorna Pettibridge. Dec 7-16th , The Lantern Works 418 Marlowe Street 555 318 4096 Black backgroud , painting effect on THE HOLLOW CLOCKWORK . Quantum physics imagery background (SEE UP LOADED FILE) disregard human image
Nice to have
• IF YOU CAN INCORPORATE A HURTLING CHRISTMAS TREE THRU SPACE (RED & GREEN LIGHTS) THAT WOULD BE FANTASTiC see upload!! Christmas tree moving thru space as rocket..
Should not have
• COLOR -Except lights on Christmas tree

```html
<!DOCTYPE html>
<html lang="en">
<head>
<meta charset="utf-8">
<title>Theatre Velunor presents The Hollow Clockwork</title>
<link rel="stylesheet" href="https://fonts.googleapis.com/css2?family=Creepster&family=Josefin+Sans:wght@300;400&family=Oswald:wght@400;500&family=Bebas+Neue&display=swap">
<style>
  :root {
    --ink: #0a0a0a;
    --ink-soft: #1b1b1b;
    --paper: #fbfbfb;
    --mist: #dddddd;
    --silver: #cbcbcb;
    --smoke: #5c5c5c;
    --charcoal: #333333;
  }
  html, body {
    margin: 0;
    padding: 0;
    width: 873px;
    height: 1200px;
    overflow: hidden;
    background: var(--ink);
  }
  .poster {
    position: relative;
    width: 873px;
    height: 1200px;
    background: var(--ink);
    color: var(--paper);
    overflow: hidden;
    text-align: center;
  }
  .quantum-field {
    position: absolute;
    inset: 0;
    background:
      radial-gradient(ellipse 38% 22% at 72% 30%, rgba(203,203,203,0.22), transparent 70%),
      radial-gradient(ellipse 30% 16% at 30% 22%, rgba(203,203,203,0.14), transparent 70%),
      radial-gradient(ellipse 12% 30% at 2% 62%, rgba(221,221,221,0.16), transparent 70%),
      radial-gradient(ellipse 12% 30% at 98% 58%, rgba(221,221,221,0.16), transparent 70%),
      radial-gradient(ellipse 60% 10% at 50% 98%, rgba(92,92,92,0.35), transparent 70%),
      linear-gradient(180deg, var(--ink-soft) 0%, var(--ink) 45%, var(--ink) 100%);
  }
  .line {
    position: absolute;
    left: 0;
    right: 0;
    margin: 0;
    line-height: 1;
    white-space: nowrap;
  }
  .company {
    top: 28px;
    font-family: "Josefin Sans", sans-serif;
    font-weight: 300;
    font-size: 34px;
    letter-spacing: 11px;
    text-transform: uppercase;
  }
  .presents {
    top: 82px;
    font-family: "Josefin Sans", sans-serif;
    font-weight: 300;
    font-size: 20px;
    letter-spacing: 3px;
    text-transform: uppercase;
  }
  .title {
    position: absolute;
    top: 360px;
    left: 0;
    right: 0;
    margin: 0;
    font-family: "Creepster", cursive;
    font-weight: 400;
    font-size: 86px;
    line-height: 96px;
    letter-spacing: 2px;
    text-transform: uppercase;
    background: linear-gradient(180deg, var(--paper) 0%, var(--paper) 55%, var(--silver) 78%, var(--smoke) 100%);
    -webkit-background-clip: text;
    background-clip: text;
    color: transparent;
  }
  .title span { display: block; }
  .byline {
    top: 680px;
    font-family: "Josefin Sans", sans-serif;
    font-weight: 400;
    font-size: 26px;
    letter-spacing: 2px;
    text-transform: uppercase;
  }
  .credits {
    position: absolute;
    top: 738px;
    left: 0;
    right: 0;
    font-family: "Oswald", sans-serif;
    text-transform: uppercase;
    line-height: 1;
  }
  .credits p { margin: 0; }
  .credits .director {
    font-weight: 500;
    font-size: 19px;
    letter-spacing: 6px;
  }
  .credits .with {
    margin-top: 5px;
    font-size: 16px;
    letter-spacing: 2px;
  }
  .credits .cast,
  .credits .video {
    margin-top: 5px;
    font-size: 18px;
    letter-spacing: 2px;
  }
  .atom {
    position: absolute;
    top: 846px;
    left: 336px;
    width: 200px;
    height: 130px;
  }
  .dates {
    top: 1036px;
    font-family: "Bebas Neue", sans-serif;
    font-size: 64px;
    letter-spacing: 7px;
  }
  .dates sup {
    font-size: 30px;
    letter-spacing: 3px;
    vertical-align: 26px;
  }
  .venue {
    top: 1116px;
    font-family: "Oswald", sans-serif;
    font-weight: 400;
    font-size: 21px;
    letter-spacing: 3px;
    text-transform: uppercase;
  }
</style>
</head>
<body>
  <main class="poster">
    <div class="quantum-field" role="img" aria-label="Black and white photograph of particle tracks: swirling spirals and looping trails across a dark field"></div>

    <p class="line company">Theatre Velunor</p>
    <p class="line presents">Presents</p>

    <h1 class="title"><span>The</span><span>Hollow</span><span>Clockwork</span></h1>

    <p class="line byline">By Victor L Marsh</p>

    <div class="credits">
      <p class="director">Directed by Martin Kesslow</p>
      <p class="with">With</p>
      <p class="cast">Caroline Westby | Tom Ashfeld | Margarett Okonroyy</p>
      <p class="video">Video design by Lorna Pettibridge</p>
    </div>

    <svg class="atom" viewBox="0 0 200 130" aria-hidden="true">
      <g fill="none" stroke="#fbfbfb" stroke-width="4">
        <ellipse cx="100" cy="65" rx="92" ry="24"/>
        <ellipse cx="100" cy="65" rx="92" ry="24" transform="rotate(60 100 65)"/>
        <ellipse cx="100" cy="65" rx="92" ry="24" transform="rotate(-60 100 65)"/>
      </g>
      <g fill="#fbfbfb">
        <circle cx="100" cy="65" r="9"/>
        <circle cx="26" cy="52" r="6"/>
        <circle cx="148" cy="117" r="6"/>
        <circle cx="142" cy="10" r="6"/>
      </g>
    </svg>

    <p class="line dates">Dec 7-16<sup>th</sup></p>
    <p class="line venue">The Lantern Works, 418 Marlowe Street 555 318-4096</p>
  </main>
</body>
</html>
```